Landscape Company Stationary
Biz cards, letterhead, envelopes, etc
Professional
Dean Morvik
P.O. Box 3852
Sparta, NJ 07634
foxridgemail@postbrim.com
Dont want address on biz cards, just letterhead and envelopes. Would like to incorporate the stripe and colors that are in our logo.
Logo with colors and fonts to use. Please incorporate the striping too and colors

```html
<!DOCTYPE html>
<html lang="en">
<head>
<meta charset="utf-8">
<title>Foxridge Landscapes – Business Cards</title>
<link rel="stylesheet" href="https://fonts.googleapis.com/css2?family=Montserrat:wght@400;600;800&display=swap">
<style>
  :root {
    --backdrop: #3b3a38;
    --card: #ffffff;
    --card-shade: #eef0ec;
    --brand-green: #3f9a2c;
    --brand-green-dark: #1f6e1c;
    --brand-lime: #8cc63f;
    --ink: #333333;
    --ink-soft: #6d6d6d;
  }
  * { margin: 0; padding: 0; box-sizing: border-box; }
  html, body { width: 1200px; height: 749px; overflow: hidden; }
  body {
    background: var(--backdrop);
    font-family: "Montserrat", Arial, sans-serif;
    position: relative;
  }
  .card {
    position: absolute;
    width: 486px;
    height: 278px;
    border-radius: 12px;
    background: linear-gradient(180deg, var(--card) 0%, var(--card-shade) 100%);
    overflow: hidden;
    box-shadow: 0 6px 18px rgba(0,0,0,0.35);
  }
  .card--front { left: 156px; top: 161px; }
  .card--back { left: 502px; top: 367px; }

  .wordmark {
    position: absolute;
    display: flex;
    flex-direction: column;
    color: var(--brand-green);
    font-weight: 800;
    line-height: 1;
  }
  .wordmark__name { font-size: 44px; letter-spacing: -0.5px; }
  .wordmark__sub { font-size: 15px; letter-spacing: 2px; text-transform: uppercase; margin-top: 4px; align-self: flex-end; }
  .wordmark__stripe {
    height: 5px;
    background: var(--brand-green);
    border-radius: 3px;
    margin-top: 4px;
  }
  .card--front .wordmark { left: 30px; top: 24px; }
  .card--back .wordmark { left: 116px; top: 96px; }

  .leaf-watermark {
    position: absolute;
    left: 272px;
    top: 92px;
    width: 130px;
    height: 120px;
    border-radius: 50%;
    background: radial-gradient(ellipse at center, rgba(200,210,195,0.45) 0%, rgba(230,235,228,0) 70%);
  }

  .contact { position: absolute; left: 24px; top: 168px; color: var(--ink); }
  .contact__name { font-size: 13px; font-weight: 800; color: var(--brand-green); }
  .contact__role { font-size: 9px; color: var(--ink-soft); margin-bottom: 12px; }
  .contact__line { font-size: 10px; line-height: 17px; }
  .contact__label { font-weight: 600; }

  .base-band {
    position: absolute;
    left: 0; right: 0; bottom: 0;
    height: 24px;
    background: var(--brand-green);
    border-top: 4px solid var(--brand-lime);
  }
  .base-notch {
    position: absolute;
    left: 398px;
    bottom: 14px;
    width: 28px;
    height: 20px;
  }
</style>
</head>
<body>
  <section class="card card--front" aria-label="Business card front">
    <div class="wordmark">
      <span class="wordmark__name">Foxridge</span>
      <span class="wordmark__sub">Landscapes</span>
      <span class="wordmark__stripe"></span>
    </div>
    <div class="leaf-watermark" role="img" aria-label="Faint leaf decoration"></div>
    <div class="contact">
      <p class="contact__name">Dean Morvik</p>
      <p class="contact__role">Owner</p>
      <p class="contact__line"><span class="contact__label">Phone:</span> 973-555-0148</p>
      <p class="contact__line"><span class="contact__label">Cell:</span> 862-555-0172</p>
      <p class="contact__line"><span class="contact__label">Email:</span> foxridgemail@postbrim.com</p>
    </div>
    <div class="base-band"></div>
    <svg class="base-notch" viewBox="0 0 28 20" aria-hidden="true">
      <polygon points="0,0 28,0 14,18" fill="var(--brand-green-dark)"/>
      <polygon points="4,0 24,0 14,12" fill="var(--brand-lime)"/>
    </svg>
  </section>

  <section class="card card--back" aria-label="Business card back">
    <div class="wordmark">
      <span class="wordmark__name">Foxridge</span>
      <span class="wordmark__sub">Landscapes</span>
      <span class="wordmark__stripe"></span>
    </div>
  </section>
</body>
</html>
```